Velvet Heel Ball Poster

We need a poster design for a local event we are holding in our town. The band playing is called "Tinsel" and the theme is "Glam Rock". We would like to see a design that ties in with the Glam Rock theme and it should be very eyecatching. I have attached a file showing the type of look that you might think is suitable but I am open to suggestions! Thanks so much - I am looking forward to seeing your ideas!!

It also needs to say on the poster that the event is sponsored by the Wandoora CRC (see attached logo) and the Wandoora Progress Association (see attached logo)

Industry/Entity Type

Town

Requirements
Must have
• Must have the following wording...

Calling all Rockers...
The Wandoora Progress Association proudly presents live music by
"Tinsel"
Friday 26th October
7:30pm
Wandoora Hall
Tickets $20 - Available from the Wandoora CRC
Dress - GLAM ROCK

```html
<!DOCTYPE html>
<html lang="en">
<head>
<meta charset="utf-8">
<title>Velvet Heel Ball Poster</title>
<link rel="stylesheet" href="https://fonts.googleapis.com/css2?family=Anton&family=Bangers&family=Comfortaa:wght@700&family=Gochi+Hand&family=Kurale&family=Rye&family=Sancreek&display=swap">
<style>
  :root {
    --bg-dark: #6e5466;
    --bg-mid: #9a8592;
    --bg-light: #d9d6d8;
    --rule: #111111;
    --headline-yellow: #f4f224;
    --ink-black: #141414;
    --rocker-purple: #9b1fb0;
    --date-orange: #d9791c;
    --time-purple: #8e1fa8;
    --venue-blue: #2b4fd6;
    --dress-pink: #ff1f7a;
    --splash-purple: #c42be0;
    --splash-pink: #f2288a;
    --glam-white: #ffffff;
    --live-purple: #8d1fcf;
    --band-pink: #f07a9c;
    --silhouette: #1a1a1a;
    --logo-white: #ffffff;
  }
  html, body {
    margin: 0;
    padding: 0;
    overflow: hidden;
    background: #ffffff;
  }
  .poster {
    position: relative;
    width: 1200px;
    height: 900px;
    overflow: hidden;
    background:
      radial-gradient(ellipse 620px 260px at 620px 520px, var(--bg-light) 0%, rgba(217,214,216,0.55) 45%, rgba(217,214,216,0) 100%),
      linear-gradient(160deg, #8a6475 0%, var(--bg-dark) 40%, var(--bg-mid) 60%, var(--bg-dark) 100%);
    font-family: "Kurale", serif;
  }
  .top-rule {
    position: absolute;
    left: 0;
    width: 1200px;
    height: 6px;
    background: var(--rule);
  }
  .top-rule--upper { top: 26px; }
  .top-rule--lower { top: 98px; }
  .presenter {
    position: absolute;
    top: 30px;
    left: 0;
    width: 1200px;
    text-align: center;
    font-family: "Kurale", serif;
    font-weight: 400;
    font-size: 48px;
    line-height: 66px;
    color: var(--headline-yellow);
    -webkit-text-stroke: 1.5px var(--ink-black);
    margin: 0;
    white-space: nowrap;
  }
  .tickets {
    position: absolute;
    top: 114px;
    left: 0;
    width: 1200px;
    text-align: center;
    margin: 0;
    font-family: "Kurale", serif;
    font-size: 26px;
    line-height: 34px;
    color: var(--glam-white);
    -webkit-text-stroke: 0.5px var(--ink-black);
  }
  .call-out {
    position: absolute;
    top: 180px;
    left: 160px;
    margin: 0;
    font-family: "Sancreek", serif;
    font-weight: 400;
    font-size: 90px;
    line-height: 1;
    color: var(--rocker-purple);
    -webkit-text-stroke: 2px var(--ink-black);
    transform: rotate(3deg);
    transform-origin: left top;
    letter-spacing: 1px;
    white-space: nowrap;
  }
  .event-details {
    position: absolute;
    left: 760px;
    top: 300px;
    font-family: "Gochi Hand", cursive;
    transform: rotate(-20deg);
    transform-origin: left top;
  }
  .event-date {
    position: absolute;
    left: 10px;
    top: 90px;
    white-space: nowrap;
    font-size: 44px;
    color: var(--date-orange);
    -webkit-text-stroke: 0.6px #5a2c00;
  }
  .event-time {
    position: absolute;
    left: 110px;
    top: 140px;
    white-space: nowrap;
    font-size: 38px;
    color: var(--time-purple);
  }
  .event-venue {
    position: absolute;
    left: 860px;
    top: 440px;
    margin: 0;
    font-family: "Gochi Hand", cursive;
    font-size: 40px;
    color: var(--venue-blue);
    white-space: nowrap;
    transform: rotate(-4deg);
    transform-origin: left top;
  }
  .glam-splash {
    position: absolute;
    left: 310px;
    top: 350px;
    width: 520px;
    height: 300px;
    border-radius: 48% 52% 40% 60% / 55% 45% 55% 45%;
    background: radial-gradient(circle at 35% 40%, var(--splash-purple) 0%, var(--splash-pink) 60%, rgba(242,40,138,0.2) 100%);
  }
  .glam-title {
    position: absolute;
    left: 400px;
    top: 410px;
    width: 340px;
    margin: 0;
    text-align: center;
    font-family: "Anton", sans-serif;
    font-size: 110px;
    line-height: 100px;
    color: var(--glam-white);
    letter-spacing: 2px;
  }
  .guitarist {
    position: absolute;
    background: linear-gradient(180deg, var(--silhouette) 0%, #2c2a2c 100%);
    border-radius: 40px 40px 10px 10px;
  }
  .guitarist--left { left: 130px; top: 460px; width: 200px; height: 255px; }
  .guitarist--right { left: 770px; top: 470px; width: 190px; height: 245px; }
  .dress-code {
    position: absolute;
    left: 710px;
    top: 570px;
    margin: 0;
    font-family: "Bangers", sans-serif;
    font-size: 58px;
    color: var(--dress-pink);
    -webkit-text-stroke: 1.5px var(--ink-black);
    transform: rotate(4deg);
    transform-origin: left top;
    white-space: nowrap;
    letter-spacing: 1px;
  }
  .live-music {
    position: absolute;
    left: 0;
    top: 718px;
    width: 1200px;
    text-align: center;
    margin: 0;
    font-family: "Comfortaa", sans-serif;
    font-size: 46px;
    color: var(--live-purple);
    -webkit-text-stroke: 0.8px var(--ink-black);
    letter-spacing: 2px;
  }
  .band-name {
    position: absolute;
    left: 0;
    top: 772px;
    width: 1200px;
    text-align: center;
    margin: 0;
    font-family: "Rye", serif;
    font-size: 78px;
    line-height: 1.1;
    color: var(--band-pink);
    -webkit-text-stroke: 1.2px var(--ink-black);
    letter-spacing: 3px;
  }
  .sponsor {
    position: absolute;
    display: flex;
    align-items: center;
    gap: 12px;
    font-family: "Kurale", serif;
    color: var(--logo-white);
    white-space: nowrap;
  }
  .sponsor--town { left: 50px; top: 828px; font-size: 38px; }
  .sponsor--crc { left: 900px; top: 830px; font-size: 34px; }
  .sponsor-mark {
    width: 22px;
    height: 22px;
    background: var(--logo-white);
  }
</style>
</head>
<body>
  <main class="poster">
    <div class="top-rule top-rule--upper"></div>
    <h2 class="presenter">The Wandoora Progress Association proudly presents</h2>
    <div class="top-rule top-rule--lower"></div>
    <p class="tickets">Tickets $20 - Available from the Wandoora CRC</p>

    <h1 class="call-out">CALLING ALL ROCKERS...</h1>

    <div class="glam-splash" role="img" aria-label="Paint splash in purple, pink and yellow halftone"></div>
    <div class="guitarist guitarist--left" role="img" aria-label="Silhouette of a guitarist"></div>
    <div class="guitarist guitarist--right" role="img" aria-label="Silhouette of a guitarist"></div>
    <p class="glam-title">GLAM<br>ROCK</p>

    <div class="event-details">
      <span class="event-date">Friday 26th October</span>
      <span class="event-time">7:30pm</span>
    </div>
    <p class="event-venue">@ Wandoora Hall</p>

    <p class="dress-code">DRESS - GLAM ROCK</p>

    <p class="live-music">live music by</p>
    <p class="band-name">"TINSEL"</p>

    <div class="sponsor sponsor--town"><span class="sponsor-mark"></span>Wandoora</div>
    <div class="sponsor sponsor--crc"><span class="sponsor-mark"></span>Wandoora CRC</div>
  </main>
</body>
</html>
```